Label Sticker Design for Apothecary Brand

Hello! We are an independent grassroots business located in Ontario, Canada that specializes in making organic botanical and herbal skin care, tea, witchcraft and wellness products. We have been in business for 5 years and are looking to create a label sticker with one of our slogans for use in packaging.

Our brand is dark, herbal, witchy, and modern with old-world apothecary and vintage influences. We want a label that will be VERY clean, and easily explain what our product is, while conveying a sense of mysticism and magic, as well as a traditional apothecary vibe.

We have attached design inspiration to give you an idea of the style that we would like. Our demographic is hipster, current, (think finger tattoos, linen dresses, and organic groceries), and they care deeply about where we source our ingredients, and how we craft our product. We don't want an old-school sticker that looks like it should be on the shelves of a health food store. The design should be contemporary, upmarket, modern and clean, but evoke a strong sense of magic and self-care with wild gathered herbs and unusual wild flowers!

This will be used as a packaging sticker for our shipping boxes.

We look forward to your winning design!
Thank you very much.

Target Market(s)

20 - 50yr Female Demographic
Natural, bohemian, earthy, hipster and modern

Key Words: Minimalist Tattoos, Organic Skin Care, Bohemian, Witchy, Dark, Moody, Confident, Sustainable, Ethical,

PLEASE VIEW PHOTOS BEFORE SUBMITTING A DESIGN ;)

Industry/Entity Type

Skin Care Product

Font styles to use
Serif
Script

Colors
1b1b1b
5c5c5c
fbfbfb

Requirements
Must have
• Clean and Simple - Take a look at the photos we've posted!
• Black / greyscale (No color)
• Label sticker must be a rectangle (3" x 2")
• Very Modern with a touch of old-world
• We are open to a variety of font styles. Please see photo FONT in image files, or the images 'Bottle Inspiration'
• Please use the following text:
• Thornmoor Stillhouse
• --------------------
• Crafted with Magic
• * Once your design is chosen and purchased, we will require the names of all fonts and sources of imagery used.
Nice to have
• A moody botanical graphic surrounding the text. Tangled wild, antique botanical illustrations. Not mandatory, but would be very nice.
Should not have
• Colour
• Messy or overly dramatic fonts
• Cartoon Imagery
• Leaf Motif
• Female Body Silhouettes
• Scroll or decorative borders.
• Butterflies, birds etc
• Actual pictures of witches
• Mandalas or Messy Graphics

```html
<!DOCTYPE html>
<html lang="en">
<head>
<meta charset="utf-8">
<title>Thornmoor Stillhouse – Label Sticker</title>
<link rel="stylesheet" href="https://fonts.googleapis.com/css2?family=UnifrakturMaguntia&family=Italianno&display=swap">
<style>
  :root {
    --ink: #1b1b1b;
    --ink-soft: #5c5c5c;
    --paper: #fbfbfb;
    --page: #ffffff;
    --texture: #d6d7d9;
    --rule: #4a4a4a;
    --art-light: #eeeeee;
    --art-dark: #bdbdbd;
  }
  * { box-sizing: border-box; margin: 0; padding: 0; }
  html, body {
    width: 1200px;
    height: 1200px;
    overflow: hidden;
    background: var(--page);
  }
  .canvas {
    position: relative;
    width: 1200px;
    height: 1200px;
  }
  .label {
    position: absolute;
    left: 69px;
    top: 273px;
    width: 1051px;
    height: 700px;
    background: var(--paper);
    border: 1px solid #e2e2e2;
    overflow: hidden;
  }
  .label__texture {
    position: absolute;
    inset: 0;
    background:
      radial-gradient(ellipse 62% 60% at 50% 50%, var(--paper) 70%, rgba(251,251,251,0) 100%),
      var(--texture);
  }
  .label__name {
    position: absolute;
    left: 0;
    right: 0;
    top: 488px;
    top: 480px;
    top: 470px;
    text-align: center;
    font-family: "UnifrakturMaguntia", serif;
    font-size: 66px;
    line-height: 1;
    color: var(--ink);
    letter-spacing: 2px;
  }
  .label__name { top: 197px; }
  .label__rule {
    position: absolute;
    left: 142px;
    top: 350px;
    width: 742px;
    border-top: 2px dashed var(--rule);
  }
  .label__tagline {
    position: absolute;
    left: 128px;
    top: 470px;
    font-family: "Italianno", cursive;
    font-size: 82px;
    line-height: 1;
    color: var(--ink);
  }
  .label__botanical {
    position: absolute;
    left: 658px;
    top: 420px;
    width: 300px;
    height: 200px;
    border-radius: 50% 50% 40% 40%;
    background: radial-gradient(ellipse at 60% 45%, var(--art-dark) 0%, var(--art-light) 70%, rgba(238,238,238,0) 100%);
  }
</style>
</head>
<body>
  <div class="canvas">
    <section class="label">
      <div class="label__texture" role="img" aria-label="Distressed grey paper texture framing the label edges"></div>
      <h1 class="label__name">Thornmoor Stillhouse</h1>
      <div class="label__rule"></div>
      <p class="label__tagline">Crafted with Magic</p>
      <div class="label__botanical" role="img" aria-label="Line illustration of a mortar and pestle beside a sprig of wild flowering herbs"></div>
    </section>
  </div>
</body>
</html>
```